Motorized Shades, Lighting, Audio Video Control systems needs a website

We need a website similar to Vornelix.com which describes our main product solutions (Motorized Shades Fabrication) lighting control and automation systems to create a convenient innovative environment with advance technology, colorful design that can provide comfort and saves on energy.
Updates

Hi Please see Sample adaptation image we need to have the site as per this website: http://www.quendaport.com/Works/index

Target Market(s)

Mid to high end residential, Commercial building, Offices, Architects

Industry/Entity Type

Environment

Font styles to use
Sans Serif

Colors
0355a3
9bcb3c
fbed24
fbf289
34a7d8
f68e4e
f37122

Requirements
Must have
• some animated slides /banners, possible virtual control of shade and lights animated
Nice to have
• we need website like http://www.quendaport.com/Works/index with content and colors adapted to our identity (see attached adaptation image)

sample websites to extract from :
Vornelix.com
wmsatel.com
pirun.it
haldimvo.com

```html
<!DOCTYPE html>
<html lang="en">
<head>
<meta charset="utf-8">
<title>Lumoran – Motorized Shades &amp; Lighting</title>
<link href="https://fonts.googleapis.com/css2?family=Open+Sans:wght@400;600;700&family=Lato:wght@300;400;700&family=Questrial&display=swap" rel="stylesheet">
<style>
:root{
  --page-bg:#ececec;
  --white:#ffffff;
  --green:#9bcb3c;
  --green-dark:#7fb82a;
  --yellow:#fbed24;
  --orange:#f68e4e;
  --orange-dark:#f05a1a;
  --blue:#34a7d8;
  --blue-dark:#1f86c6;
  --text:#444444;
  --text-soft:#555555;
  --brand-ink:#4a4a4a;
  --rule:#cfcfcf;
}
*{margin:0;padding:0;box-sizing:border-box}
html,body{width:1099px;height:1200px;overflow:hidden}
body{
  position:relative;
  background:radial-gradient(ellipse at 50% 40%,#ffffff 0%,#f3f3f3 45%,var(--page-bg) 100%);
  font-family:"Lato",sans-serif;color:var(--text);
}
.sheet{position:absolute;left:104px;top:0;width:890px;height:878px;background:var(--white);box-shadow:0 0 8px rgba(0,0,0,.06)}
.top-links{position:absolute;right:27px;top:11px;font:600 12px "Open Sans",sans-serif;color:#555;word-spacing:2px}
.top-links span{margin:0 8px;color:#777}
.brand{position:absolute;left:34px;top:44px}
.brand-name{font:400 40px/1 "Open Sans",sans-serif;color:var(--brand-ink);letter-spacing:.5px}
.search{position:absolute;left:623px;top:62px;width:245px;height:30px;border:1px solid #c9c9c9;border-radius:15px;font:italic 12px "Open Sans",sans-serif;color:#888;padding:7px 0 0 16px}
.search svg{position:absolute;right:10px;top:7px}
.nav{position:absolute;left:0;top:109px;width:890px;height:45px;background:linear-gradient(#a4d449,var(--green-dark));display:flex;padding-left:37px}
.nav a{font:600 14.5px/45px "Open Sans",sans-serif;color:#fff;text-decoration:none;margin-right:35px}
.hero{position:absolute;left:0;top:154px;width:890px;height:380px;background:#000;overflow:hidden}
.hero-photo{position:absolute;left:360px;top:0;width:530px;height:380px;
  background:linear-gradient(90deg,#000 0%,#2b2a26 20%,#6d6556 45%,#b9ad93 70%,#d8d1c2 100%)}
.hero-copy{position:absolute;left:50px;top:110px;color:#fff}
.hero-copy h1{font:400 35px/1 "Questrial",sans-serif;letter-spacing:.5px}
.hero-copy h2{font:400 22px/1 "Questrial",sans-serif;margin-top:10px}
.hero-copy p{font:400 13px/21px "Open Sans",sans-serif;color:#ccc;margin-top:10px;width:440px}
.btn{display:inline-block;margin-top:15px;margin-left:2px;width:115px;height:29px;border-radius:15px;background:var(--yellow);color:#111;font:600 12.5px/29px "Open Sans",sans-serif;text-align:center}
.about{position:absolute;left:0;top:562px;width:890px;text-align:center}
.about h2{font:300 30px/1 "Lato",sans-serif;color:#333}
.about p{font:400 11.8px/20px "Lato",sans-serif;color:var(--text-soft);margin:8px auto 0;width:805px}
.about p+p{margin-top:5px}
.cards{position:absolute;left:13px;top:701px;display:flex;gap:9px}
.card{position:relative;width:283px;height:161px;border-radius:3px;color:#fff;padding:22px 0 0 20px}
.card h3{font:400 21.5px/1 "Open Sans",sans-serif}
.card .lead{font:400 12.5px/1 "Open Sans",sans-serif;margin-top:9px}
.card .note{font:400 9.6px/15px "Open Sans",sans-serif;opacity:.8;margin-top:8px;width:135px}
.card .more{font:700 10.5px/1 "Open Sans",sans-serif;margin-top:11px;margin-left:1px;display:flex;align-items:center;gap:4px}
.card-orange{background:linear-gradient(#f68e4e,var(--orange-dark))}
.card-blue{background:linear-gradient(#55bde6,var(--blue-dark))}
.card-green{background:linear-gradient(#aed65a,var(--green-dark))}
.card-pic{position:absolute}
.footer-cols{position:absolute;left:0;top:921px;width:1099px}
.col{position:absolute;top:0}
.col h4{font:300 18px/1 "Lato",sans-serif;color:#333;margin-bottom:9px}
.col li{list-style:none;font:400 12.2px/24.5px "Lato",sans-serif;color:#444}
.col li strong{font-weight:700;color:#333}
.rule{position:absolute;left:104px;top:1118px;width:891px;height:1px;background:var(--rule)}
.copyright{position:absolute;left:104px;top:1142px;font:400 12.2px "Lato",sans-serif;color:#555}
.social{position:absolute;left:889px;top:1137px;display:flex;gap:7px}
.social span{width:20px;height:20px;border-radius:2px;background:#8a8a8a}
</style>
</head>
<body>
<div class="sheet">
  <div class="top-links">Register<span>|</span>Product Quick Links<span>|</span>Login</div>
  <div class="brand"><div class="brand-name">Lumoran</div></div>
  <div class="search">Search here..
    <svg width="16" height="16" viewBox="0 0 16 16"><circle cx="6.5" cy="6.5" r="4.8" fill="none" stroke="#888" stroke-width="2.2"/><line x1="10" y1="10" x2="14" y2="14" stroke="#888" stroke-width="2.6" stroke-linecap="round"/></svg>
  </div>
  <nav class="nav">
    <a>Home</a><a>About Us</a><a>Products</a><a>Our Services</a><a>Lighting</a><a>Support</a><a>Career</a><a>Support</a><a>Contact</a>
  </nav>
  <section class="hero">
    <div class="hero-photo" role="img" aria-label="Photo of a modern living room with motorized shades and warm recessed lighting"></div>
    <div class="hero-copy">
      <h1>Motorized Shades &amp; Lighting</h1>
      <h2>Etiam est nunc venenatis tristique</h2>
      <p>Ut nisi erat fermentum vel congue id euismod in elit Fusce ultricies orci ac feugiat suscipit leo massa sodales velit et scelerisqu</p>
      <span class="btn">Learn More</span>
    </div>
  </section>
  <section class="about">
    <h2>Little About Our Company</h2>
    <p>Morbi eget arcu Morbi porta libero id ullamcorper nonummy nibh ligula pulvinar metus eget consectetuer augue nisi quis lacus Ut ac mi quis lacus mollis aliquam Curabitur iaculis tempus eros Curabitur vel mi sit amet magna malesuada ultrices Ut nisi erat fermentum vel congue id euismod in elit</p>
    <p>Donec scelerisque leo ac risus Praesent sit amet est In dictum dolor eu dictum porttitor enim felis viverra mi</p>
  </section>
  <div class="cards">
    <div class="card card-orange">
      <h3>Lightings</h3><div class="lead">Morbi eget arcu porta</div>
      <div class="note">Vivamus porttitor &nbsp;purus<br>nisi eleifend libero</div>
      <div class="more">READ MORE <svg width="6" height="8"><path d="M0 0L6 4L0 8Z" fill="#fff"/></svg></div>
      <div class="card-pic" role="img" aria-label="Photo of a wall-mounted touch control panel" style="left:154px;top:23px;width:118px;height:113px;background:linear-gradient(#f4f4f4,#dcdcdc);padding:12px"><div style="width:100%;height:100%;background:linear-gradient(#2d4a5a,#1a7fa0)"></div></div>
    </div>
    <div class="card card-blue">
      <h3>Audio &amp; Video</h3><div class="lead">Morbi eget arcu porta</div>
      <div class="note">Vivamus porttitor g purus nisi eleifend libero a tempus</div>
      <div class="more">READ MORE <svg width="6" height="8"><path d="M0 0L6 4L0 8Z" fill="#fff"/></svg></div>
      <div class="card-pic" role="img" aria-label="Photo of a black audio video receiver" style="left:157px;top:78px;width:116px;height:55px;border-radius:4px;background:linear-gradient(160deg,#3a3a3a,#0c0c0c)"></div>
    </div>
    <div class="card card-green">
      <h3>Lighting Product</h3><div class="lead">Morbi eget arcu porta</div>
      <div class="note">Vivamus porttitor g purus nisi eleifend libero a tempus</div>
      <div class="more">READ MORE <svg width="6" height="8"><path d="M0 0L6 4L0 8Z" fill="#fff"/></svg></div>
      <div class="card-pic" role="img" aria-label="Photo of a white wall dimmer switch" style="left:199px;top:27px;width:67px;height:107px;border-radius:3px;background:linear-gradient(#ffffff,#e6e6e6)"></div>
    </div>
  </div>
</div>

<div class="footer-cols">
  <div class="col" style="left:109px"><h4>Company</h4><ul><li>Ammy nibh ligula</li><li>Pulvinar metus eget</li><li>Consectetuer augue</li><li>Nisi quis lacus</li></ul></div>
  <div class="col" style="left:290px"><h4>About Us</h4><ul><li>Llibero lectus feugiat</li><li>Felis Morbi</li><li>Diam mauris viverra</li><li>Gravida eu mattis</li><li>Morbi eget arcu</li></ul></div>
  <div class="col" style="left:482px"><h4>Services</h4><ul><li>Ammy nibh ligula</li><li>Pulvinar metus eget</li><li>Diam mauris viverra</li><li>Gravida eu mattis</li><li>Morbi eget arcu</li></ul></div>
  <div class="col" style="left:666px"><h4>Resources</h4><ul><li>Ammy nibh ligula</li><li>Pulvinar metus eget</li><li>Consectetuer augue</li><li>Nisi quis lacus</li></ul></div>
  <div class="col" style="left:838px"><h4>Technical Support</h4><ul><li>Support Online</li><li style="line-height:16px"><strong>1.800.555.0142 (24/7)</strong></li><li style="margin-top:8px">Sales Support</li><li style="line-height:16px"><strong>1.800.555.0178 (24/7)</strong></li></ul></div>
</div>
<div class="rule"></div>
<div class="copyright">© 2014 Company Name. &nbsp;All right reserved. &nbsp;Term of Use</div>
<div class="social" aria-label="Social links"><span></span><span></span><span></span><span></span></div>
</body>
</html>
```